Audio Visual & Broadcast Installing Company needs a Web Site Design

We need a website design for our company Corvane Ltd. We are a small company that does Audio Visual and broadcast installations. We are looking to expand our business and need a professional web presence. All work completed by us is done to a very high standard and it’s this attention to detail that sets us apart from our competitors. Our projects include doing fibre optics at major sporting events; installing and commissioning bespoke control systems on super yachts and installing the latest systems in luxury homes.

We provide the following services:
System design
On-site installation
Rack building
Pre-fabricated cable looms
Fibre optic cabling

We would like a website that gives details of our services and provides contact information. Our customers are other businesses and our website needs to reflect this. The flyer attached will be used to promote the company and we would like the website to follow this theme. Please use the colours from our logo, as the colour scheme. We know that our colours are bright and we don’t want them to overwhelm the site. With our website we want to communicate that we are professional and provide a quality service.
NB UPDATE: please use stock images for any graphical elements.

The following 3 sites belong to some of our competitors. The first 2, we DON'T like because they don't project a professional feeling. The last one, 'vellumspire', is better as it provides the required information in a clear, simple form.

http://www.plomquist-example.com/

http://www.heronfieldlinkworks-example.com/

http://www.vellumspire-example.com/

We really like the following site, it feels professional and high end without too many flashy graphics. We want something that is fast to load but still shows the high end quality of our work.

http://osmerdalegroup-example.com/

Pages/Sections

Home
On site installation
Rack building and cable looms
Fibre optics
Portfolio (this will be limited to start with but must be easy to expand and add new projects)
Updates

Target Market(s)

Businesses operating in the following areas:
Audio Vision, Broadcasting, Home Automation, Events

Industry/Entity Type

Broadcasting

Coding

Coded - Design and coding required

Number of Pages Required

4 page

Font styles to use
Other font styles liked:
• similar to attached flyer

Requirements
Must have
• The same theme as the 'flyer1' attachment.

```html
<!DOCTYPE html>
<html lang="en">
<head>
<meta charset="utf-8">
<title>Corvane Ltd — Audio Visual &amp; Broadcast Installation</title>
<link href="https://fonts.googleapis.com/css2?family=Roboto:wght@400;500;700&family=Tinos:wght@700&display=swap" rel="stylesheet">
<style>
  :root {
    --ink: #333333;
    --topbar: #2b2b2b;
    --footer: #333333;
    --white: #ffffff;
    --nav-active: #e6e6e6;
    --blue-1: #1a82f5;
    --blue-2: #3d98f5;
    --blue-3: #5ba9f7;
    --blue-4: #7ab9f9;
    --blue-5: #96c7fb;
    --arrow: #1a82f5;
    --logo-mark: #e0263b;
  }
  * { box-sizing: border-box; margin: 0; padding: 0; }
  html, body { width: 1140px; height: 1200px; overflow: hidden; background: var(--white); }
  body { font-family: "Roboto", Arial, sans-serif; color: var(--ink); position: relative; }

  .hero {
    position: absolute; left: 0; top: 0; width: 1140px; height: 596px;
    background:
      radial-gradient(ellipse at 50% 40%, rgba(235,225,240,.9) 0%, rgba(180,175,205,.7) 30%, rgba(60,70,120,0) 65%),
      linear-gradient(180deg, #1d2650 0%, #5b6290 25%, #a9a6c4 45%, #6b7090 62%, #3a5a3a 72%, #6faa3a 85%, #4f8a2a 100%);
  }
  .hero-copy { position: absolute; top: 256px; left: 0; width: 1184px; text-align: center; }
  .hero-lead { font-size: 21px; line-height: 26px; color: #3a3a3a; }
  .hero-strong { margin-top: 14px; font-size: 22px; font-weight: 700; letter-spacing: 1px; color: #2e2e2e; }
  .hero-note { font-size: 10px; color: #333; }
  .hero-dots { position: absolute; top: 483px; left: 536px; display: flex; gap: 8px; }
  .hero-dots span { width: 12px; height: 12px; border-radius: 50%; background: var(--white); }
  .hero-dots span.active { background: transparent; border: 1px solid #555; box-shadow: inset 0 0 0 2px var(--white); }

  .topbar {
    position: absolute; left: 136px; top: 0; width: 892px; height: 24px;
    background: var(--topbar); color: var(--white); font-size: 10px;
    display: flex; justify-content: space-between; align-items: center; padding: 0 34px 0 38px;
  }
  .topbar span { display: flex; align-items: center; gap: 8px; }

  .header {
    position: absolute; left: 136px; top: 24px; width: 892px; height: 85px;
    background: var(--white); display: flex; justify-content: space-between;
  }
  .brand { display: flex; align-items: center; gap: 12px; padding-left: 38px; }
  .brand-mark { width: 30px; height: 30px; background: var(--logo-mark); }
  .brand-name { font-size: 22px; font-weight: 500; color: #333; }
  .nav { display: flex; height: 85px; padding-right: 24px; }
  .nav a { display: flex; align-items: center; padding: 0 12px; font-size: 12px; letter-spacing: .4px; color: #222; text-decoration: none; }
  .nav a.active { background: var(--nav-active); font-weight: 700; width: 90px; justify-content: center; margin-right: 4px; }

  .services { position: absolute; left: 136px; top: 509px; width: 892px; height: 220px; display: flex; }
  .service { flex: 0 0 178.4px; padding: 24px 10px 0 38px; color: var(--white); }
  .service:nth-child(1) { background: var(--blue-1); }
  .service:nth-child(2) { background: var(--blue-2); padding-left: 31px; }
  .service:nth-child(3) { background: var(--blue-3); padding-left: 43px; }
  .service:nth-child(4) { background: var(--blue-4); padding-left: 23px; }
  .service:nth-child(5) { background: var(--blue-5); padding-left: 26px; }
  .service svg { display: block; height: 36px; }
  .service .rule { width: 27px; height: 2px; background: var(--white); margin: 10px 0 12px; }
  .service h3 { font-size: 13.5px; font-weight: 500; line-height: 16px; height: 36px; }
  .service p { font-size: 11.5px; line-height: 14px; margin-top: 2px; max-width: 118px; }

  .portfolio-title {
    position: absolute; top: 766px; left: 0; width: 1160px;
    display: flex; justify-content: center; align-items: center; gap: 14px;
    font-family: "Tinos", "Times New Roman", serif; font-size: 22px; letter-spacing: 1.5px; color: #333;
  }
  .portfolio-title::before, .portfolio-title::after { content: ""; width: 45px; height: 3px; background: #333; }

  .work { position: absolute; top: 820px; height: 240px; }
  .work-1 { left: 137px; width: 304px; background: linear-gradient(135deg, #2f7fd8, #4d97ea 60%, #3a86dd); display: flex; flex-direction: column; align-items: center; justify-content: center; }
  .work-2 { left: 467px; width: 268px; background: linear-gradient(135deg, #c9a83a, #3a9a6a 50%, #1f6a7a); }
  .work-3 { left: 761px; width: 268px; background: radial-gradient(circle at 50% 55%, #6a8ab0, #203a78 55%, #0e1d4a); }
  .work-1 .label { color: var(--white); font-size: 12.5px; font-weight: 700; letter-spacing: .8px; margin-top: 8px; }

  .pager { position: absolute; top: 1086px; left: 936px; display: flex; gap: 9px; }
  .pager span { width: 42px; height: 42px; background: var(--arrow); display: flex; align-items: center; justify-content: center; }

  .footer {
    position: absolute; left: 0; top: 1153px; width: 1140px; height: 47px;
    background: var(--footer); color: var(--white); font-size: 11.5px; letter-spacing: .3px;
    display: flex; justify-content: space-between; align-items: center; padding: 0 111px 0 136px;
  }
  .footer-nav span.sep { margin: 0 11px; }
</style>
</head>
<body>

<div class="hero" role="img" aria-label="Floodlit stadium at night with a striped green pitch under a cloudy sky"></div>
<div class="hero-copy">
  <p class="hero-lead">Broadcasting the Harrowmere Open was equally<br>thrilling as playing the Harrowmere Open</p>
  <p class="hero-strong">AND WE DELIVERED</p>
  <p class="hero-note">*as cabling partners for broadcast televions</p>
</div>
<div class="hero-dots"><span class="active"></span><span></span><span></span></div>

<div class="topbar">
  <span>
    <svg width="10" height="10" viewBox="0 0 24 24" fill="#fff"><path d="M6.6 10.8a15 15 0 0 0 6.6 6.6l2.2-2.2a1 1 0 0 1 1-.25 11.4 11.4 0 0 0 3.6.57 1 1 0 0 1 1 1V20a1 1 0 0 1-1 1A17 17 0 0 1 3 4a1 1 0 0 1 1-1h3.5a1 1 0 0 1 1 1c0 1.25.2 2.45.57 3.57a1 1 0 0 1-.25 1z"/></svg>
    01632-555-0147
  </span>
  <span>
    <svg width="13" height="9" viewBox="0 0 13 9"><rect width="13" height="9" fill="#fff"/><path d="M0 0l6.5 5L13 0" stroke="#2b2b2b" fill="none"/></svg>
    info@corvane-example.com
  </span>
</div>

<header class="header">
  <div class="brand"><span class="brand-mark"></span><span class="brand-name">Corvane</span></div>
  <nav class="nav">
    <a class="active" href="#">HOME</a>
    <a href="#">INSTALLATION</a>
    <a href="#" style="padding-right:22px">SERVICES</a>
    <a href="#">PORTFOLIO</a>
    <a href="#">CONTACT US</a>
  </nav>
</header>

<section class="services">
  <div class="service">
    <svg viewBox="0 0 36 40" width="32" fill="none" stroke="#fff" stroke-width="2"><path d="M6 18a13 13 0 0 1 24 0"/><path d="M10 18a8.5 8.5 0 0 1 16 0"/><circle cx="18" cy="16" r="2.5" fill="#fff"/><path d="M18 19l-5 19M18 19l5 19M14.5 31h7"/></svg>
    <div class="rule"></div>
    <h3>Broadcast/<br>AV System Design</h3>
    <p>Corvane provides cabling services for Broadcast Television and audio visual systems, With over 15 years experience .</p>
  </div>
  <div class="service">
    <svg viewBox="0 0 36 36" width="30" fill="#fff"><path d="M15 2h6l1 5 4 2 4-3 4 4-3 4 2 4 5 1v6l-5 1-2 4 3 4-4 4-4-3-4 2-1 5h-6l-1-5-4-2-4 3-4-4 3-4-2-4-5-1v-6l5-1 2-4-3-4 4-4 4 3 4-2z" transform="scale(.9) translate(1 1)"/><circle cx="17" cy="17" r="5" fill="#3d98f5"/></svg>
    <div class="rule"></div>
    <h3>On-site Installation</h3>
    <p>Corvane provides cabling services for Broadcast Television and audio visual systems, With over 15 years experience .</p>
  </div>
  <div class="service">
    <svg viewBox="0 0 30 36" width="30" fill="#fff"><rect y="8" width="30" height="5"/><rect y="15" width="30" height="5"/><rect y="22" width="30" height="5"/><rect x="3" y="10" width="2" height="1" fill="#5ba9f7"/><rect x="3" y="17" width="2" height="1" fill="#5ba9f7"/><rect x="3" y="24" width="2" height="1" fill="#5ba9f7"/></svg>
    <div class="rule"></div>
    <h3>Rack Building</h3>
    <p>Corvane provides cabling services for Broadcast Television and audio visual systems, With over 15 years experience .</p>
  </div>
  <div class="service">
    <svg viewBox="0 0 32 36" width="32" fill="none" stroke="#fff" stroke-width="1.6"><rect x="2" y="3" width="20" height="30"/><path d="M2 13l10-10M2 21l18-18M2 29l20-20M8 33l14-14M16 33l6-6"/><path d="M22 28c6 0 8 3 6 5"/></svg>
    <div class="rule"></div>
    <h3>Pre-fabrication Cable Looms</h3>
    <p>Corvane provides cabling services for Broadcast Television and audio visual systems, With over 15 years experience .</p>
  </div>
  <div class="service">
    <svg viewBox="0 0 24 36" width="24" fill="none" stroke="#fff" stroke-width="1.5"><path d="M12 22V8M12 22l-5-12M12 22l5-12M12 22l-8-8M12 22l8-8"/><rect x="8" y="22" width="8" height="11" fill="#fff"/></svg>
    <div class="rule"></div>
    <h3>Fibre optics<br>Installation</h3>
    <p>Corvane provides cabling services for Broadcast Television and audio visual systems, With over 15 years experience .</p>
  </div>
</section>

<h2 class="portfolio-title">PORTFOLIO</h2>

<div class="work work-1" role="img" aria-label="Technicians in hard hats working at a cabling cabinet, shown under a blue hover overlay">
  <svg width="30" height="30" viewBox="0 0 30 30" fill="none" stroke="#fff" stroke-width="2"><circle cx="13" cy="13" r="10"/><path d="M20.5 20.5L28 28M13 8v10M8 13h10"/></svg>
  <span class="label">INSTALLATION PROCESS</span>
</div>
<div class="work work-2" role="img" aria-label="Hands patching yellow fibre cables into a green patch panel"></div>
<div class="work work-3" role="img" aria-label="Close-up of a fibre optic cable with coloured inner strands on a blue background"></div>

<div class="pager">
  <span><svg width="14" height="20" viewBox="0 0 14 20" fill="none" stroke="#fff" stroke-width="3.5"><path d="M11 2L3 10l8 8"/></svg></span>
  <span><svg width="14" height="20" viewBox="0 0 14 20" fill="none" stroke="#fff" stroke-width="3.5"><path d="M3 2l8 8-8 8"/></svg></span>
</div>

<footer class="footer">
  <div class="footer-nav">HOME<span class="sep">|</span>INSTALLATION<span class="sep">|</span>SERVICES<span class="sep">|</span>PORTFOLIO<span class="sep">|</span>CONTACT US</div>
  <div>COPYRIGHT@2017 CORVANE, ALL RIGHT RESERVED</div>
</footer>

</body>
</html>
```